Business Card Design

Art work over image with business name and phone number. We do automotive wire repair. Some sort of auto theme. Thanks!
Updates

I would like to see the images I uploaded in the card.  Thanks!

Target Market(s)

Auto body repair shops

Industry/Entity Type

Automotive

Contact Information for Business Card

VOLTLINE PROS

602-555-0193

Requirements
Nice to have
• Raised lettering?

```html
<!DOCTYPE html>
<html lang="en">
<head>
<meta charset="utf-8">
<title>Voltline Pros – Business Card</title>
<link href="https://fonts.googleapis.com/css2?family=Orbitron:wght@400;700;900&display=swap" rel="stylesheet">
<style>
  :root {
    --page: #ffffff;
    --card: #0d0e10;
    --card-edge: #1b1c1f;
    --band: #050506;
    --band-line: #2a2c30;
    --brand-blue: #1f8fe6;
    --ink: #e9ecef;
    --ink-soft: #c9ced4;
    --art-deep: #0b3f8a;
    --art-glow: #2fa8ff;
  }
  * { box-sizing: border-box; margin: 0; padding: 0; }
  html, body { width: 1200px; height: 900px; overflow: hidden; background: var(--page); }
  body { position: relative; font-family: "Orbitron", sans-serif; }

  .card {
    position: absolute;
    top: 270px;
    width: 530px;
    height: 330px;
    border-radius: 22px;
    overflow: hidden;
    background: var(--card);
    color: var(--ink);
  }
  .card--front { left: 28px; }
  .card--back { left: 642px; }

  .card__backdrop {
    position: absolute; inset: 0;
    background: radial-gradient(ellipse at 35% 40%, #2a2c31 0%, #16171a 45%, var(--card) 100%);
  }

  .band {
    position: absolute; left: 0; right: 0;
    background: var(--band);
    border-top: 1px solid var(--band-line);
    border-bottom: 1px solid var(--band-line);
    opacity: .92;
  }
  .card--front .band { top: 222px; height: 62px; }
  .card--back .band { top: 112px; height: 112px; }

  .brand {
    position: absolute;
    font-weight: 900;
    color: var(--brand-blue);
    letter-spacing: 1px;
    white-space: nowrap;
  }
  .card--front .brand { top: 52px; left: 62px; font-size: 38px; }
  .card--back .brand { right: 26px; bottom: 28px; font-size: 27px; }

  .contact {
    position: absolute;
    display: flex; align-items: center; gap: 12px;
    font-size: 24px; font-weight: 400; letter-spacing: 2px;
    color: var(--ink);
    white-space: nowrap;
  }
  .contact svg { flex: none; }
  .card--front .contact--phone { left: 50px; top: 233px; font-size: 26px; }
  .card--back .contact--phone { left: 90px; top: 124px; }
  .card--back .contact--email { left: 52px; top: 176px; font-size: 20px; letter-spacing: 1px; text-transform: uppercase; }
  .card--back .divider {
    position: absolute; left: 0; right: 0; top: 168px; height: 1px; background: var(--band-line);
  }

  .tagline {
    position: absolute; left: 38px; bottom: 14px;
    font-size: 13px; letter-spacing: 12px;
    color: var(--ink-soft);
    text-transform: uppercase;
    white-space: nowrap;
  }

  .car-art {
    position: absolute; right: 8px; top: 118px;
    width: 180px; height: 150px;
    border-radius: 40% 45% 30% 30%;
    background: radial-gradient(ellipse at 50% 65%, var(--art-glow) 0%, var(--art-deep) 55%, rgba(11,63,138,0) 75%);
  }
</style>
</head>
<body>

  <section class="card card--front">
    <div class="card__backdrop" role="img" aria-label="Dark photo of automotive wiring connectors"></div>
    <div class="car-art" role="img" aria-label="Illustration of a glowing blue wireframe car with spilling auto parts"></div>
    <h1 class="brand">VOLTLINE PROS</h1>
    <div class="band"></div>
    <p class="contact contact--phone">
      <svg width="36" height="36" viewBox="0 0 36 36" aria-hidden="true">
        <circle cx="18" cy="18" r="16" fill="none" stroke="#e9ecef" stroke-width="2"/>
        <path d="M12 10c1-1 2-1 3 0l2 3c.5 1 0 2-1 2.5-.5.5 0 2 1.5 3.5s3 2 3.5 1.5c.5-1 1.5-1.5 2.5-1l3 2c1 1 1 2 0 3-2 2-5 2-9-2s-4-7-5.5-9.5z" fill="#e9ecef"/>
      </svg>
      602-555-0193
    </p>
    <p class="tagline">Automotive wire repair</p>
  </section>

  <section class="card card--back">
    <div class="card__backdrop" role="img" aria-label="Dark photo of automotive wiring connectors"></div>
    <div class="band"></div>
    <div class="divider"></div>
    <p class="contact contact--phone">
      <svg width="32" height="32" viewBox="0 0 36 36" aria-hidden="true">
        <circle cx="18" cy="18" r="16" fill="none" stroke="#e9ecef" stroke-width="2"/>
        <path d="M12 10c1-1 2-1 3 0l2 3c.5 1 0 2-1 2.5-.5.5 0 2 1.5 3.5s3 2 3.5 1.5c.5-1 1.5-1.5 2.5-1l3 2c1 1 1 2 0 3-2 2-5 2-9-2s-4-7-5.5-9.5z" fill="#e9ecef"/>
      </svg>
      602-555-0193
    </p>
    <p class="contact contact--email">
      <svg width="32" height="32" viewBox="0 0 36 36" aria-hidden="true">
        <circle cx="18" cy="18" r="16" fill="none" stroke="#e9ecef" stroke-width="2"/>
        <rect x="9" y="12" width="18" height="12" fill="none" stroke="#e9ecef" stroke-width="1.6"/>
        <path d="M9 12l9 7 9-7" fill="none" stroke="#e9ecef" stroke-width="1.6"/>
      </svg>
      mike.dorran@voltmail.net
    </p>
    <p class="brand">VOLTLINE PROS</p>
  </section>

</body>
</html>
```